Vast Ledger Web Design - For local online shopping 'village'

URGENTLY REQUIRE WEB DESIGNER FOR VAST LEDGER WEB STORE - CODING REQUIRED

REQUIREMENT; BE ABLE TO TALK ENGLISH VERY WELL AS THIS WILL BE AN ON GOING PROJECT

(WE WILL BE TALKING ON TALKLOOM OR CHIRPLINE)

The business name is 'Holmwyck's - Corvale's Online Shopping Village'
(PICS ATTACHED FOR LAYOUT DEMONSTRATION PURPOSES)

I need a draft of the website operational within 7 days to show potential clients. The remainder may take an additional 7+ days to complete. Can discuss further payments due to the work involved.

It's an online shopping village where individual shop owners have the ability to place their store (logo) and their products on this website to increase exposure to their business and more importantly their online delivery service.

The site will need to be structured in a very easy to use manner. Customers ages will range from 18+ to 80+.

THE IMAGINATION, FEEL & PRESENCE OF THE WEB PAGE;
You are a professional web designer, I will need you to use your imagination and add pieces to this website that I can't see. My vision and feel for this website is based on the grocery stores that were able to survive and thrive during the late stages of WWII. A lot of design now and with future marketing & advertising will be revolved and the 1940's feel & look. I'm happy to hear your thoughts on things we can add or improve on in the site. It's very basic now and it's more warmth and character.

THE LAYOUT;
The first page will have a white brick wallpaper background (pic attached as 'wallpaper'. This will be the wallpaper used for the entire site. The business logo (hasn't been made yet - waiting on drafts) will be at the top of the page and beneath it will be 3 categories to choose from (in the final stage it will have 6 categories).

DRAFT STAGE;
1. Village grocers (pic attached ' vgrocers') (To be written ' Village Grocers written on the frame burnt into the wood or written underneath the frame - must be large and clear to read')
2. Butchers (pic attached 'vbutcher')(as above - Village butchers)
3. Seafood (pic attached 'VSF')(as above Seafood)
They will all require framing (pic attached 'frame')
I'd like the images to be slightly bouncy if you put your mouse or finger on the logo.

Once the customer enters their choice it will then take them to their desired category.

NEXT PAGE:

Main focus is in the Grocers section; The same design structure will appear (business logo 'Holmwyck - Corvale's online shopping village'.
2 business choices will be available in this section. Their logos are attached ('PDNQ' and 'Mundey's Grocer') I'd like you to enhance the logo's with more depth and background shadow - please don't spend to much time but make them look better. I'd like the logo's to be slightly bouncy if you put your mouse or finger on the logo. The wallpaper used will be 'wallpaper'.

PLEASE NOTE: Could you please remove the logo from the background image of 'PDNQ'.

For the draft stage we will focus on 'PDNQ'. Once you click on PDNQ it will take you to their page. The wallpaper will be the same as the brick wallpaper on the other 2 pages. The logo of 'PDNQ' will be placed boldly at the top middle of the page. On this page there will be 4 categories to choose from. Everything will be the same, wallpaper will be white brick, the categories (pics attached as Deli, Fruit&Veg, Bakery & Pantry ) they will need to be framed and the category name will be burnt into the wood or placed underneath.

This is where we stop for the time being.

I've attached layout pictures, so you can see what I see. Please add all the little things i've added to the layout pictures that i haven't written here..

Example: Our Mission, Contact us, Home delivery.. etc.

The site will need to continue to grow as we fill the categories with products and add more businesses to the site.. so on and so on. It's an ongoing job and we will need good communication and understanding with each other.

Please do what you can to show your vision in line with what i've written above. If you'd like to contact me feel free to do so, we can organize a talk on talkloom if need be.

All the best & I hope you are all safe and healthy!

Odo

Industry/Entity Type

Online Store

Coding

Coded - Design and coding required

Number of Pages Required

5+ page

Requirements
Must have
• Looks like the 1940's merged with the modern age.
Nice to have
• Age some nice grocery store touches. 1940's + grocery stores had things hanging from the walls, ornaments here and there. It felt homely. Add some things or talk about the things that you're thinking about adding.

```html
<!DOCTYPE html>
<html lang="en">
<head>
<meta charset="utf-8">
<title>Holmwyck's – Corvale's Online Shopping Village</title>
<link href="https://fonts.googleapis.com/css2?family=Lato:wght@400;700;900&display=swap" rel="stylesheet">
<style>
  :root {
    --wall-light: #f7f7f6;
    --wall-mid: #e9e9e7;
    --ink: #111111;
    --wood-dark: #5a3a1e;
    --wood: #80552e;
    --wood-light: #9c6c3e;
    --string: #b59a72;
    --nail: #6e6e6e;
    --band: #cdb9a1;
    --band-light: #dccbb6;
    --band-edge: #ece3d7;
    --nav-ink: #1e1a16;
    --social: #1a1a1a;
  }
  * { margin: 0; padding: 0; box-sizing: border-box; }
  html, body { width: 1200px; height: 674px; overflow: hidden; }
  body {
    position: relative;
    font-family: 'Lato', sans-serif;
    color: var(--ink);
    background: radial-gradient(ellipse at 50% 35%, var(--wall-light) 0%, var(--wall-mid) 100%);
  }
  .brand {
    position: absolute; top: 30px; left: 0; width: 1200px;
    text-align: center;
  }
  .brand-name {
    font-weight: 900; font-size: 60px; line-height: 1; letter-spacing: -0.5px;
  }
  .brand-tagline {
    font-weight: 700; font-size: 19px; margin-top: 2px; letter-spacing: 0.1px;
  }
  .category {
    position: absolute; top: 178px; width: 270px;
    text-decoration: none; color: var(--ink);
  }
  .category-frame { position: relative; width: 270px; height: 250px; }
  .category-frame svg { position: absolute; left: 0; top: 0; }
  .category-photo {
    position: absolute; left: 38px; top: 80px; width: 196px; height: 134px;
  }
  .photo-grocers { background: linear-gradient(135deg, #1e2a22 0%, #3f6b2a 35%, #d0542c 60%, #27301f 100%); }
  .photo-butchers { background: linear-gradient(135deg, #2a2625 0%, #b46c69 40%, #d99a8f 60%, #2b2827 100%); }
  .photo-seafood { background: linear-gradient(135deg, #bcd0dc 0%, #4f6b82 35%, #c74a33 60%, #d9e4ea 100%); }
  .category-label {
    text-align: center; font-weight: 700; font-size: 22px; margin-top: 12px;
  }
  .footer-band { position: absolute; left: 0; top: 540px; width: 1200px; height: 134px; }
  .footer-nav {
    position: absolute; top: 620px; left: 0; width: 1200px; height: 22px;
  }
  .footer-nav a {
    position: absolute; transform: translateX(-50%);
    color: var(--nav-ink); text-decoration: none; font-size: 15.5px; white-space: nowrap;
  }
  .social {
    position: absolute; left: 1010px; top: 606px; width: 106px; text-align: center;
  }
  .social-title { font-size: 14.5px; color: var(--nav-ink); }
  .social-list { display: flex; justify-content: center; gap: 7px; margin-top: 6px; }
  .social-list a {
    display: block; width: 15px; height: 15px; border-radius: 2px; background: var(--social);
  }
</style>
</head>
<body>
  <header class="brand">
    <h1 class="brand-name">Holmwyck's</h1>
    <p class="brand-tagline">Corvale's Online Shopping Village</p>
  </header>

  <a class="category" href="#grocers" style="left:148px">
    <div class="category-frame">
      <svg width="270" height="250" viewBox="0 0 270 250" aria-hidden="true">
        <polyline points="42,54 134,6 228,54" fill="none" stroke="var(--string)" stroke-width="3"/>
        <circle cx="134" cy="6" r="4" fill="var(--nail)"/>
        <rect x="6" y="44" width="32" height="204" fill="var(--wood)"/>
        <rect x="232" y="44" width="32" height="204" fill="var(--wood)"/>
        <rect x="0" y="52" width="270" height="28" fill="var(--wood-light)" stroke="var(--wood-dark)" stroke-width="2"/>
        <rect x="0" y="214" width="270" height="28" fill="var(--wood-light)" stroke="var(--wood-dark)" stroke-width="2"/>
      </svg>
      <div class="category-photo photo-grocers" role="img" aria-label="Fresh vegetables and fruit on a dark wooden board"></div>
    </div>
    <p class="category-label">Village Grocers</p>
  </a>

  <a class="category" href="#butchers" style="left:465px">
    <div class="category-frame">
      <svg width="270" height="250" viewBox="0 0 270 250" aria-hidden="true">
        <polyline points="42,54 134,6 228,54" fill="none" stroke="var(--string)" stroke-width="3"/>
        <circle cx="134" cy="6" r="4" fill="var(--nail)"/>
        <rect x="6" y="44" width="32" height="204" fill="var(--wood)"/>
        <rect x="232" y="44" width="32" height="204" fill="var(--wood)"/>
        <rect x="0" y="52" width="270" height="28" fill="var(--wood-light)" stroke="var(--wood-dark)" stroke-width="2"/>
        <rect x="0" y="214" width="270" height="28" fill="var(--wood-light)" stroke="var(--wood-dark)" stroke-width="2"/>
      </svg>
      <div class="category-photo photo-butchers" role="img" aria-label="Raw cuts of meat on a dark butcher's board"></div>
    </div>
    <p class="category-label">Butchers</p>
  </a>

  <a class="category" href="#seafood" style="left:781px">
    <div class="category-frame">
      <svg width="270" height="250" viewBox="0 0 270 250" aria-hidden="true">
        <polyline points="42,54 134,6 228,54" fill="none" stroke="var(--string)" stroke-width="3"/>
        <circle cx="134" cy="6" r="4" fill="var(--nail)"/>
        <rect x="6" y="44" width="32" height="204" fill="var(--wood)"/>
        <rect x="232" y="44" width="32" height="204" fill="var(--wood)"/>
        <rect x="0" y="52" width="270" height="28" fill="var(--wood-light)" stroke="var(--wood-dark)" stroke-width="2"/>
        <rect x="0" y="214" width="270" height="28" fill="var(--wood-light)" stroke="var(--wood-dark)" stroke-width="2"/>
      </svg>
      <div class="category-photo photo-seafood" role="img" aria-label="Fresh fish, octopus and lobster on ice"></div>
    </div>
    <p class="category-label">Seafood</p>
  </a>

  <svg class="footer-band" width="1200" height="134" viewBox="0 0 1200 134" aria-hidden="true">
    <path d="M0,14 L40,10 L70,4 L110,12 L160,8 L210,14 L260,9 L320,15 L380,10 L440,16 L500,11 L560,17 L620,12 L680,18 L740,13 L800,16 L860,11 L920,17 L980,12 L1040,16 L1100,10 L1160,15 L1200,12 L1200,134 L0,134 Z" fill="var(--band-edge)"/>
    <path d="M0,22 L50,18 L90,24 L140,16 L200,26 L260,20 L330,28 L400,22 L470,30 L540,24 L610,31 L680,25 L750,30 L820,24 L890,30 L960,23 L1030,29 L1100,22 L1160,28 L1200,24 L1200,134 L0,134 Z" fill="var(--band-light)"/>
    <path d="M0,34 L60,30 L130,38 L200,32 L280,40 L360,34 L440,42 L520,36 L600,43 L680,37 L760,42 L840,36 L920,42 L1000,35 L1080,41 L1150,34 L1200,38 L1200,134 L0,134 Z" fill="var(--band)"/>
  </svg>

  <nav class="footer-nav">
    <a href="#home" style="left:400px">Home</a>
    <a href="#mission" style="left:494px">Our Mission</a>
    <a href="#delivery" style="left:619px">Home Delivery</a>
    <a href="#faq" style="left:716px">FAQ</a>
    <a href="#contact" style="left:793px">Contact</a>
  </nav>

  <div class="social">
    <p class="social-title">Join the Village</p>
    <div class="social-list">
      <a href="#social-1" aria-label="Social page one"></a>
      <a href="#social-2" aria-label="Social page two"></a>
      <a href="#social-3" aria-label="Social page three"></a>
      <a href="#social-4" aria-label="Social page four"></a>
    </div>
  </div>
</body>
</html>
```